Quarrow financial services, is a financial company that provides consultancy, brokerage services, and funding.

we will be providing the clients with insights, knowledge and data with regards to the financial markets.

with the brokerage services we will try to find the suitable counterparts that provide them with the best investments that suits their needs and expected return.

Target Market(s)

financial institutions, Corporates, high-net worth individuals

Industry/Entity Type

Financial Service

Contact Information for Business Card

Font styles to use
Other font styles liked:
• applemyungjo

Colors
00a990
848484

Requirements
Must have
• the logo at the back
Nice to have
• Finesse
Should not have
• boldness

```html
<!DOCTYPE html>
<html lang="en">
<head>
<meta charset="utf-8">
<title>Quarrow Financial Services – Business Card</title>
<link rel="stylesheet" href="https://fonts.googleapis.com/css2?family=Cormorant+Garamond:wght@400&family=Open+Sans:wght@300;400&display=swap">
<style>
  :root {
    --teal: #00a990;
    --teal-light: #22cfc2;
    --grey: #848484;
    --ink: #5b6266;
    --paper: #ffffff;
    --paper-shade: #eeeeee;
    --backdrop: #e6e3dd;
  }
  * { box-sizing: border-box; margin: 0; padding: 0; }
  html, body { width: 1200px; height: 858px; overflow: hidden; }
  body {
    background: var(--backdrop);
    font-family: "Open Sans", Arial, sans-serif;
    position: relative;
  }
  .card {
    position: absolute;
    width: 540px;
    height: 309px;
    background: var(--paper);
    box-shadow: 0 6px 20px rgba(0,0,0,.18);
    overflow: hidden;
  }
  .card--front { left: 50px; top: 110px; }
  .card--back {
    left: 610px; top: 440px;
    background: radial-gradient(ellipse at 45% 40%, #ffffff 0%, #f2f2f2 100%);
  }

  .brand__name {
    font-family: "Cormorant Garamond", Georgia, serif;
    font-weight: 400;
    color: var(--ink);
    letter-spacing: 2px;
    text-transform: uppercase;
    line-height: 1.1;
    white-space: nowrap;
  }
  .tagline {
    font-family: "Open Sans", Arial, sans-serif;
    font-weight: 300;
    color: var(--grey);
    letter-spacing: 1px;
    white-space: nowrap;
  }

  /* front */
  .front__top {
    position: absolute; left: 0; top: 0; width: 100%; height: 120px;
    display: flex; flex-direction: column; align-items: flex-end; justify-content: center;
    gap: 8px;
    padding-right: 30px;
  }
  .front__top .brand__name { font-size: 25px; }
  .front__top .tagline { font-size: 10px; }
  .front__panel {
    position: absolute; left: 0; top: 120px; width: 100%; height: 189px;
    background: var(--paper-shade);
  }
  .person { position: absolute; left: 26px; top: 26px; }
  .person__name { font-size: 19px; font-weight: 300; color: var(--grey); }
  .person__role { font-size: 15px; font-weight: 300; color: var(--teal); margin-top: -2px; }
  .contacts {
    position: absolute; left: 230px; right: 0; top: 20px;
    list-style: none;
  }
  .contacts__item {
    height: 38px; margin-bottom: 12px;
    background: linear-gradient(90deg, var(--teal) 0%, var(--teal-light) 100%);
    display: flex; align-items: center; gap: 12px;
    padding-left: 14px;
    color: #fff; font-size: 15px; font-weight: 400;
  }
  .contacts__icon {
    width: 24px; height: 24px; background: #fff; border-radius: 4px;
    display: flex; align-items: center; justify-content: center;
  }

  /* back */
  .back__brand {
    position: absolute; inset: 0;
    display: flex; flex-direction: column; align-items: center; justify-content: center;
    gap: 12px;
  }
  .back__brand .brand__name { font-size: 32px; }
  .back__brand .tagline { font-size: 12px; }
</style>
</head>
<body>

<section class="card card--front" aria-label="Business card front">
  <div class="front__top">
    <p class="brand__name">Quarrow Financial Services</p>
    <p class="tagline">Clear insight for every market choice</p>
  </div>
  <div class="front__panel">
    <div class="person">
      <p class="person__name">Elias Varner</p>
      <p class="person__role">owner</p>
    </div>
    <ul class="contacts">
      <li class="contacts__item">
        <span class="contacts__icon">
          <svg width="16" height="16" viewBox="0 0 16 16"><circle cx="8" cy="8" r="3" fill="none" stroke="#00a990" stroke-width="1.6"/><path d="M11 8v1.5a2 2 0 0 0 3 0V8a6 6 0 1 0-2.5 4.9" fill="none" stroke="#00a990" stroke-width="1.6"/></svg>
        </span>
        info@quarrowfs.com
      </li>
      <li class="contacts__item">
        <span class="contacts__icon">
          <svg width="16" height="16" viewBox="0 0 16 16"><rect x="4" y="1.5" width="8" height="13" rx="1.5" fill="none" stroke="#00a990" stroke-width="1.6"/><line x1="7" y1="12" x2="9" y2="12" stroke="#00a990" stroke-width="1.6"/></svg>
        </span>
        555-014-2280
      </li>
      <li class="contacts__item">
        <span class="contacts__icon">
          <svg width="16" height="16" viewBox="0 0 16 16"><path d="M2 8 8 2.5 14 8M4 7v7h8V7" fill="none" stroke="#00a990" stroke-width="1.6"/></svg>
        </span>
        480 N Linden Ave
      </li>
    </ul>
  </div>
</section>

<section class="card card--back" aria-label="Business card back">
  <div class="back__brand">
    <p class="brand__name">Quarrow Financial Services</p>
    <p class="tagline">Clear insight for every market choice</p>
  </div>
</section>

</body>
</html>
```